fieldscoutingpath.com - Social Media Branding

fieldscoutingpath.com --> Social Media Re-Branding & Graphics
Facebook: @fldscoutpath - Instagram: @fieldscoutingpath - Twitter: @fldscoutpath

Looking to find a good designer to help with my fieldscoutingpath.com social media sites!
- facebook banner
- twitter banner
- instagram template (square and banner size)
- Quote or Information Template
- Committed Template (uniformed) - see the ones I made (& i am no professional) at fieldscoutingpath.com/committed - needs to have fieldscoutingpath.com logo, room for: the committed school and the team the player plays on.

Also willing to pay extra for a graphic that is the "complete package" that detail all of the steps of the recruiting process detailed in fieldscoutingpath.com

Font styles to use
Sans Serif

Colors
ec1f27
fbee3e

```html
<!DOCTYPE html>
<html lang="en">
<head>
<meta charset="utf-8">
<title>Field Scouting Path – Social Media Re-Branding Case Study</title>
<link href="https://fonts.googleapis.com/css2?family=Open+Sans:ital,wght@0,300;0,400;0,600;0,700;0,800;1,300&family=Dancing+Script:wght@700&display=swap" rel="stylesheet">
<style>
:root{
  --red:#EC1F27;
  --red-light:#F26268;
  --yellow:#FBEE3E;
  --yellow-light:#FCF378;
  --orange:#F7941D;
  --ink:#111111;
  --text:#2e2e2e;
  --muted:#8a8a8a;
  --white:#ffffff;
  --paper:#ffffff;
}
*{box-sizing:border-box;margin:0;padding:0}
html,body{width:1200px;height:3125px;overflow:hidden;background:var(--paper)}
body{font-family:"Open Sans",Arial,sans-serif;color:var(--text);position:relative}
.abs{position:absolute}

/* header */
.brand{position:absolute;display:flex;align-items:center;gap:8px;font-weight:700;color:var(--ink)}
.brand-dot{border-radius:50%;background:var(--yellow);flex:none}
.header-brand{left:87px;top:52px;font-size:19px}
.header-brand .brand-dot{width:26px;height:26px}
.title-pill{left:415px;top:44px;width:696px;height:52px;border-radius:26px;
  background:linear-gradient(90deg,var(--red),var(--red-light));color:var(--white);
  font-weight:700;font-size:22px;display:flex;align-items:center;justify-content:center}

.intro{left:87px;top:121px;width:1030px;font-size:18.5px;line-height:31px}

.section{position:absolute;left:55px;width:1060px}
.section h2{position:relative;font-size:22.5px;font-weight:700;letter-spacing:1.2px;color:var(--ink);padding-left:32px;line-height:29px}
.section h2::before{content:"";position:absolute;left:0;top:6px;width:18px;height:18px;background:var(--red);box-shadow:-2px -2px 0 var(--yellow)}
.section h2 .hl{color:var(--red)}
.section .points{padding-left:32px;margin-top:16px;font-size:18.5px;line-height:31.2px}

/* style guide */
.label{position:absolute;font-size:28px;font-weight:300;color:#555}
.label::after{content:"";position:absolute;left:0;bottom:-10px;width:60px;height:5px;background:var(--red)}
.specimen{left:87px;top:1168px;font-size:140px;font-weight:700;color:var(--ink);line-height:1}
.font-name{left:87px;top:1328px;font-size:26px;font-weight:700;color:var(--ink)}
.sample{left:87px;width:520px;font-size:19px;line-height:26px;letter-spacing:1.2px;color:var(--ink)}

.swatch{position:absolute;width:84px;text-align:center}
.swatch .chip{width:84px;height:84px;border-radius:8px;box-shadow:0 3px 6px rgba(0,0,0,.18)}
.swatch .name{margin-top:8px;font-size:12.5px;font-weight:700;color:#555;white-space:nowrap;margin-left:-30px;margin-right:-30px}
.swatch .name i{font-weight:400;font-style:italic;color:#999}
.swatch .hex{font-size:10.5px;color:#999;white-space:nowrap;margin-left:-30px;margin-right:-30px}

.redesign-head{left:87px;top:1562px;font-size:27px;font-weight:300;color:#555}
.redesign-head .hl{color:var(--red)}
.redesign-head::after{content:"";position:absolute;left:0;bottom:-10px;width:60px;height:5px;background:var(--red)}

.card{position:absolute;overflow:hidden;box-shadow:0 2px 8px rgba(0,0,0,.22);background:var(--white)}
.photo{position:absolute}

/* post: did you know */
.post-fact{left:87px;top:1644px;width:432px;height:430px}
.post-fact .brand{left:14px;top:190px;font-size:17px;flex-direction:column;align-items:flex-start;gap:4px}
.post-fact .brand .brand-dot{width:36px;height:36px;margin-left:60px}
.fact-title{left:10px;top:268px;font-size:35px;font-weight:800;color:var(--red)}
.fact-text{left:10px;top:320px;font-size:22px;line-height:28px;color:#333}
.handle-box{position:absolute;top:392px;width:115px;height:22px;border:1px solid #ccc;display:flex;align-items:center;gap:8px;font-size:9.5px;color:#333}
.handle-box::before{content:"";width:16px;height:20px;background:var(--red)}

/* post: congratulations */
.post-congrats{left:87px;top:2099px;width:432px;height:430px}
.frame-line{position:absolute;inset:10px;border:2px solid rgba(255,255,255,.85);pointer-events:none}
.badge{position:absolute;background:var(--white);border-radius:6px}
.congrats-title{right:22px;top:312px;font-size:33px;font-weight:800;color:var(--yellow)}
.congrats-name{right:30px;top:352px;font-family:"Dancing Script",cursive;font-size:28px;color:var(--white)}
.footer-handles{position:absolute;display:flex;justify-content:space-between;color:var(--white);font-size:10px}
.footer-handles span{display:flex;align-items:center;gap:6px}
.footer-handles span::before{content:"";width:13px;height:13px;border-radius:50%;border:2px solid currentColor}

/* post: event */
.post-event{left:87px;top:2563px;width:421px;height:421px;background:linear-gradient(120deg,var(--red) 0%,#F04A24 45%,var(--orange) 75%,var(--yellow) 100%)}
.logo-tile{position:absolute;background:var(--white);display:flex;align-items:center;justify-content:center;gap:6px;font-weight:700;color:var(--ink)}
.post-event .logo-tile{left:0;top:0;width:104px;height:104px;border-radius:0 0 36px 0;flex-direction:column;font-size:9.5px}
.post-event .logo-tile .brand-dot{width:24px;height:24px;border-radius:50%;background:var(--yellow)}
.event-band{left:0;top:190px;width:300px;height:54px;background:var(--white);padding-left:24px;font-size:50px;font-weight:800;color:var(--ink);line-height:54px}
.event-sub{left:26px;top:266px;font-size:16px;font-weight:700;color:var(--white)}
.event-body{left:26px;top:290px;width:200px;font-size:7.5px;line-height:9.5px;color:var(--white)}
.event-address{left:26px;top:340px;display:flex;gap:8px;color:var(--white);font-size:7px;line-height:9px}
.join-now{left:292px;top:322px;padding:5px 12px;background:var(--red);color:var(--white);font-weight:800;font-size:15px;transform:rotate(-14deg);border:2px solid var(--white)}
.event-phone{left:302px;top:372px;color:var(--white);font-weight:800;font-size:14px}

/* post: admission */
.post-admission{left:548px;top:2432px;width:553px;height:554px}
.post-admission .logo-tile{left:343px;top:24px;width:185px;height:46px;border-radius:8px;font-size:14px}
.post-admission .logo-tile .brand-dot{width:22px;height:22px;border-radius:50%;background:var(--yellow)}
.adm-title{right:26px;top:84px;text-align:right;color:var(--white);font-size:44px;font-weight:800;line-height:52px}
.adm-rule{right:26px;height:4px;background:var(--yellow)}
.adm-date{right:26px;top:232px;color:var(--yellow);font-size:24px;font-weight:800}
.adm-line{position:absolute;right:26px;display:flex;align-items:center;gap:14px;color:var(--white);font-size:23px;font-weight:600}
.adm-line::before{content:"";width:22px;height:22px;border-radius:50%;background:var(--white)}
.adm-line.web{font-size:18px}
.adm-contact{right:26px;top:482px;color:var(--white);font-size:30px;font-weight:800}

/* complete package */
.package{left:548px;top:1644px;width:564px;height:749px}
.package-frame{position:absolute;left:22px;top:22px;right:22px;bottom:22px;border:1.5px dashed var(--red-light)}
.pk-title{left:46px;top:40px;font-size:16.5px;font-weight:700;color:var(--red)}
.pk-desc{left:46px;top:64px;width:220px;font-size:10px;line-height:12.5px;color:#444}
.package .brand{left:400px;top:42px;flex-direction:column;gap:4px;font-size:13.5px}
.package .brand .brand-dot{width:34px;height:34px}
.pk-heading{position:absolute;display:flex;gap:6px;color:var(--red);font-weight:700;font-size:13.5px;line-height:17px}
.pk-heading::before{content:"";flex:none;width:10px;height:10px;margin-top:3px;background:var(--red);box-shadow:-2px -2px 0 var(--yellow)}
.pk-list{left:48px;top:158px;width:282px;list-style:none;font-size:9.6px;line-height:13.2px;color:#333}
.pk-list li{position:relative;padding-left:8px;margin-bottom:8.2px}
.pk-list li::before{content:"";position:absolute;left:0;top:5px;width:3px;height:3px;border-radius:50%;background:var(--red)}
.pk-list b{color:var(--ink)}
.module{position:absolute;left:281px;width:192px;height:22px;border:1px solid #ddd;border-radius:11px;display:flex;align-items:center;gap:8px;font-size:9.5px;font-weight:700;color:#222}
.module svg{flex:none;margin-left:-2px}
.pk-cta{left:176px;top:684px;width:206px;height:24px;background:var(--yellow);display:flex;align-items:center;justify-content:center;font-size:9px;font-weight:700;color:var(--ink)}

.thanks{left:0;width:1200px;top:3040px;text-align:center;font-size:26px;font-weight:300;font-style:italic;color:#555}
</style>
</head>
<body>

<div class="brand header-brand"><span class="brand-dot"></span>fieldscoutingpath.com</div>
<div class="abs title-pill">Social Media Re-Branding Case Study on Field Scouting Path</div>

<p class="abs intro">Dear Sir / Madam, I have prepared a short case study on your brand, identified the problems &amp; then used my design as well as marketing knowledge to improve your posts / designs, thus &nbsp;improving &nbsp;your Brand's Presence on social media. Please have a look, I hope that you will like my solutions. Thanks.</p>

<section class="section" style="top:233px">
  <h2>Problems with your current social media posts/designs?</h2>
  <div class="points">
    <p>- There isn't any fixed &amp; defined color theme on your posts. Well defined color &amp; theme creates a sense of popular &amp; recognizable brand on the customer's mind.</p>
    <p>- Font choices aren't fixed &amp; defined either.</p>
    <p>- Photo/Graphics sizes aren't constant.</p>
    <p>- In some cases, designs are not clean. Clean &amp; Minimal design lets you convey the message to the consumer easily.</p>
    <p>- Every design is of different design style. This is a massive disadvantage, as consistent design styles helps customer recognize the brand at a glance.</p>
  </div>
</section>

<section class="section" style="top:529px">
  <h2>What are your competitors doing different than you?</h2>
  <div class="points" style="margin-top:8px">
    <p>- Using fixed colors &amp; following a fixed design theme.</p>
    <p>- Posting regularly on all of the social media platforms.</p>
    <p>- Their designs are much cleaner.</p>
    <p>- Following all the modern design trends.</p>
    <p>- Using appropriate sizing for the graphics.</p>
  </div>
</section>

<section class="section" style="top:757px">
  <h2>How I intend to solve those problems with <span class="hl">MODERN</span>, <span class="hl">EYE-CATCHING</span>, <span class="hl">ATTRACTIVE</span> &amp; <span class="hl">AUDIENCE ENGAGING</span> design:</h2>
  <div class="points" style="margin-top:16px">
    <p>- Use fixed &amp; well defined colors which were suggested by you on your briefing. Also introducing gradients to bring in a twist in the coloring.</p>
    <p>- Defining a good font to be used in the designs which is easily readable, clear, modern and free to use.</p>
    <p>- Using appropriate sizing for every platform in the Images/Graphics so that the message is delivered loud &amp; clear.</p>
    <p>- Clean &amp; minimalistic &amp; modern design. Deliver the message, no extra clutter.</p>
    <p>- Following all the modern design trends.</p>
  </div>
</section>

<section class="section" style="top:1050px">
  <h2>Now have a look at my approach in solving the problem:</h2>
</section>

<div class="label" style="left:87px;top:1105px">Typography</div>
<div class="abs specimen">Aa</div>
<div class="abs font-name">Font: Open Sans</div>
<p class="abs sample" style="top:1383px">FIELDSCOUTINGPATH.COM LINKS THE LESSONS, TALENT AND SKILLS TO THE COLLEGE COACHES.</p>
<p class="abs sample" style="top:1448px">fieldscoutingpath.com links the lessons, talent and skills to the college coaches.</p>

<div class="label" style="left:653px;top:1105px">Colors: Solid &amp; Gradient</div>

<div class="swatch" style="left:653px;top:1236px"><div class="chip" style="background:var(--yellow)"></div><div class="name">Yellow</div><div class="hex">#FBEE3E</div></div>
<div class="swatch" style="left:773px;top:1236px"><div class="chip" style="background:var(--yellow-light)"></div><div class="name">Yellow <i>Light</i></div><div class="hex">#FCF378</div></div>
<div class="swatch" style="left:888px;top:1236px"><div class="chip" style="background:var(--red)"></div><div class="name">Red</div><div class="hex">#EC1F27</div></div>
<div class="swatch" style="left:1009px;top:1236px"><div class="chip" style="background:var(--red-light)"></div><div class="name">Red <i>Light</i></div><div class="hex">#F26268</div></div>

<div class="swatch" style="left:657px;top:1382px"><div class="chip" style="background:linear-gradient(45deg,var(--red),var(--yellow))"></div><div class="name">Yellow + Red</div><div class="hex">#FBEE3E + #EC1F27</div></div>
<div class="swatch" style="left:773px;top:1382px"><div class="chip" style="background:linear-gradient(45deg,var(--red-light),var(--yellow-light))"></div><div class="name">Yellow + Red <i>(Light)</i></div><div class="hex">#F26268 + #FCF378</div></div>
<div class="swatch" style="left:888px;top:1380px"><div class="chip" style="background:linear-gradient(45deg,var(--red),var(--red-light))"></div><div class="name">Red + Red <i>Light</i></div><div class="hex">#EC1F27 + #F26268</div></div>
<div class="swatch" style="left:1009px;top:1380px"><div class="chip" style="background:linear-gradient(45deg,var(--yellow),var(--yellow-light))"></div><div class="name">Yellow + Yellow <i>Light</i></div><div class="hex">#F26268 + #FCF378</div></div>

<div class="abs redesign-head">Some of your posts that I've <span class="hl">REDESIGNED</span> also created a graphic for "<span class="hl">COMPLETE PACKAGE</span>"</div>

<!-- Did You Know post -->
<article class="card post-fact">
  <svg class="abs" style="left:0;top:0" width="432" height="330" viewBox="0 0 432 330">
    <defs><linearGradient id="factPhoto" x1="0" y1="0" x2="1" y2="1"><stop offset="0" stop-color="#7b8a5a"/><stop offset=".5" stop-color="#b23a3a"/><stop offset="1" stop-color="#5c5a55"/></linearGradient></defs>
    <polygon points="20,95 62,24 105,95" fill="var(--yellow-light)"/>
    <path role="img" aria-label="Photo of a softball batter in a red uniform mid-swing" d="M140,0 H432 V305 C395,300 380,265 350,248 C300,218 240,222 205,185 C165,140 175,60 140,0 Z" fill="url(#factPhoto)"/>
    <path d="M140,0 C175,60 165,140 205,185 C240,222 300,218 350,248 C380,265 395,300 432,305" fill="none" stroke="var(--yellow)" stroke-width="9"/>
  </svg>
  <div class="brand"><span class="brand-dot"></span>fieldscoutingpath.com</div>
  <div class="abs fact-title">Did You Know ?</div>
  <p class="abs fact-text">There are over 2 MILLION<br>Dollars in Softball Scholarships!</p>
  <div class="handle-box" style="left:10px">@fldscoutpath</div>
  <div class="handle-box" style="left:152px">@fldscoutpath</div>
  <div class="handle-box" style="left:295px">@fldscoutpath</div>
</article>

<!-- Congratulations post -->
<article class="card post-congrats">
  <div class="photo" role="img" aria-label="Photo of a pitcher in a purple and orange uniform winding up" style="inset:0;background:linear-gradient(160deg,#b9c2a0 0%,#8f9a6e 40%,#7a6a9a 70%,#9aa07a 100%)"></div>
  <svg class="abs" style="left:0;top:0" width="432" height="430" viewBox="0 0 432 430">
    <defs><linearGradient id="congratsRed" x1="0" y1="0" x2="0" y2="1"><stop offset="0" stop-color="var(--red-light)"/><stop offset="1" stop-color="var(--red)"/></linearGradient></defs>
    <polygon points="0,150 130,322 432,162 432,430 0,430" fill="url(#congratsRed)"/>
    <polygon points="118,312 432,146 432,166 140,322" fill="var(--yellow)"/>
  </svg>
  <div class="badge" style="left:18px;top:18px;width:100px;height:52px"></div>
  <div class="badge" style="left:334px;top:26px;width:80px;height:46px"></div>
  <div class="logo-tile" style="left:325px;top:246px;width:86px;height:50px;border-radius:6px;flex-direction:column;gap:2px;font-size:7.5px"><span class="brand-dot" style="width:16px;height:16px;border-radius:50%;background:var(--yellow)"></span>fieldscoutingpath.com</div>
  <div class="abs congrats-title">Congratulations</div>
  <div class="abs congrats-name">Avery Collins</div>
  <div class="footer-handles" style="left:18px;right:18px;top:392px"><span>@fldscoutpath</span><span>@fldscoutpath</span><span>@fldscoutpath</span></div>
  <div class="frame-line"></div>
</article>

<!-- Event post -->
<article class="card post-event">
  <div class="abs" role="img" aria-label="Circular photo of three players smiling together" style="left:140px;top:17px;width:286px;height:286px;border-radius:50%;background:linear-gradient(135deg,#5a4a3a,#2a2a2a 50%,#c9b58a);border:6px solid #1a1a1a"></div>
  <div class="logo-tile"><span class="brand-dot"></span>fieldscoutingpath.com</div>
  <div class="abs event-band">Event</div>
  <div class="abs" role="img" aria-label="Small softball illustration" style="left:366px;top:268px;width:46px;height:46px;border-radius:50%;background:var(--red);border:3px solid var(--yellow)"></div>
  <div class="abs event-sub">Example Text</div>
  <p class="abs event-body">Join us for a day of drills, coaching tips and meetups with college recruiters this season.</p>
  <div class="abs event-address">
    <svg width="20" height="26" viewBox="0 0 20 26"><path d="M10 1C5 1 1.5 4.6 1.5 9.3 1.5 15.5 10 25 10 25s8.5-9.5 8.5-15.7C18.5 4.6 15 1 10 1z" fill="none" stroke="#fff" stroke-width="2.4"/><circle cx="10" cy="9.5" r="3" fill="none" stroke="#fff" stroke-width="2"/></svg>
    <span>123 Lorem Ipsum Street<br>Lorem Ipsum Dolor Sit Amet<br>Your City, 12345</span>
  </div>
  <div class="abs join-now">JOIN NOW!</div>
  <div class="abs event-phone">+12 555-01234</div>
  <div class="footer-handles" style="left:24px;right:24px;top:402px;font-size:6px"><span>@fldscoutpath</span><span>@fldscoutpath</span><span>@fldscoutpath</span><span>fieldscoutingpath.com</span></div>
</article>

<!-- Complete package -->
<article class="card package">
  <div class="package-frame"></div>
  <div class="abs pk-title">The COMPLETE Recruiting Package</div>
  <p class="abs pk-desc">This package provides everything you will need to ensure a "W" in the Win column at the end of your recruiting journey!</p>
  <div class="brand"><span class="brand-dot"></span>fieldscoutingpath.com</div>
  <div class="pk-heading" style="left:32px;top:126px">INCLUDED IN THIS COURSE:</div>
  <ul class="abs pk-list">
    <li><b>Welcome:</b> Introduction to Instructor &amp; Course Objectives</li>
    <li><b>Recruiting Process:</b> Importance of Understanding the Process, Recruiting Rules &amp; Recruiting Calendar</li>
    <li><b>Target List of Schools:</b> Creating a list of schools that meet your academic and athletic needs</li>
    <li><b>Email &amp; Contact College Coaches:</b> When to contact coaches and what to say</li>
    <li><b>Videos:</b> What to include in your videos</li>
    <li><b>Camps &amp; Clinics:</b> What camps to attend and what to do before attending</li>
    <li><b>Social Media:</b> Why social media is important and how to use it to get recruited</li>
    <li><b>Showcase Event:</b> What showcases to attend and how to prepare</li>
    <li><b>College Visits:</b> How to prepare for both an unofficial and official college visit</li>
  </ul>
  <div class="abs" role="img" aria-label="Illustration of a cartoon batter in a red circle with Softball hand lettering" style="left:350px;top:142px;width:176px;height:230px;border-radius:88px 88px 20px 20px;background:linear-gradient(180deg,var(--red) 0%,var(--red-light) 60%,#ffffff 100%)"></div>
  <div class="abs" role="img" aria-label="Illustration of a cartoon pitcher in a red circle with Softball hand lettering" style="left:46px;top:457px;width:172px;height:232px;border-radius:86px 86px 20px 20px;background:linear-gradient(180deg,var(--red) 0%,var(--red-light) 60%,#ffffff 100%)"></div>
  <div class="pk-heading" style="left:267px;top:455px;width:250px">PLUS YOU GET ACCESS TO ALL THE RECRUITING MODULES BELOW:</div>
  <div class="module" style="top:491px"><svg width="22" height="22" viewBox="0 0 22 22"><circle cx="11" cy="11" r="11" fill="var(--red)"/><path d="M6 11.5l3.2 3.2L16 8" fill="none" stroke="#fff" stroke-width="2.2"/></svg>Parent Recruiting Guide</div>
  <div class="module" style="top:521px"><svg width="22" height="22" viewBox="0 0 22 22"><circle cx="11" cy="11" r="11" fill="var(--red)"/><path d="M6 11.5l3.2 3.2L16 8" fill="none" stroke="#fff" stroke-width="2.2"/></svg>Starter Pack</div>
  <div class="module" style="top:552px"><svg width="22" height="22" viewBox="0 0 22 22"><circle cx="11" cy="11" r="11" fill="var(--red)"/><path d="M6 11.5l3.2 3.2L16 8" fill="none" stroke="#fff" stroke-width="2.2"/></svg>Monthly Lesson</div>
  <div class="module" style="top:582px"><svg width="22" height="22" viewBox="0 0 22 22"><circle cx="11" cy="11" r="11" fill="var(--red)"/><path d="M6 11.5l3.2 3.2L16 8" fill="none" stroke="#fff" stroke-width="2.2"/></svg>Get the Offer</div>
  <div class="module" style="top:612px"><svg width="22" height="22" viewBox="0 0 22 22"><circle cx="11" cy="11" r="11" fill="var(--red)"/><path d="M6 11.5l3.2 3.2L16 8" fill="none" stroke="#fff" stroke-width="2.2"/></svg>How to Commit</div>
  <div class="module" style="top:643px"><svg width="22" height="22" viewBox="0 0 22 22"><circle cx="11" cy="11" r="11" fill="var(--red)"/><path d="M6 11.5l3.2 3.2L16 8" fill="none" stroke="#fff" stroke-width="2.2"/></svg>You Said "Yes"...What's Next?</div>
  <div class="abs pk-cta">SIGN UP &amp; START THE PROCESS TODAY!</div>
</article>

<!-- Admission post -->
<article class="card post-admission">
  <div class="photo" role="img" aria-label="Photo of a young player in a red jersey walking with her glove" style="inset:0;background:linear-gradient(90deg,#6f7d55 0%,#8b6a4a 25%,#c23b2e 42%,var(--red) 55%,#F25A22 72%,var(--orange) 88%,#F9C22E 100%)"></div>
  <div class="logo-tile"><span class="brand-dot"></span>fieldscoutingpath.com</div>
  <div class="abs adm-title">ADMISSION<br>GOING ON</div>
  <div class="abs adm-rule" style="top:198px;width:220px"></div>
  <div class="abs adm-date">1-16 JUNE</div>
  <div class="adm-line" style="top:290px">@fldscoutpath</div>
  <div class="adm-line" style="top:329px">@fldscoutpath</div>
  <div class="adm-line" style="top:368px">@fldscoutpath</div>
  <div class="adm-line web" style="top:410px">fieldscoutingpath.com</div>
  <div class="abs adm-contact">CONCTACT US</div>
  <div class="abs adm-rule" style="top:524px;width:118px"></div>
  <div class="frame-line"></div>
</article>

<p class="abs thanks">Thanks a lot for watching / reading.</p>

</body>
</html>
```